Cover for Every door Opens Where Every Door Opens

Book Cover Request
Format: Print and electronic (Quillmart)
Book Title: Every Door Opens Where Every Door Opens: Practical Roadmap for Courage and Progress
Author: R.K. Vantreel
Description: This self-help book, written by me, a self-proclaimed nobody, is filled with actionable insights and proven strategies that can help anyone. It combines humor with a serious undertone to deliver practical advice without the typical "self-helpy" vibe.
Catchphrase for the Cover: "Go from Oh Shit to Crushing It!" (or something similar)
Style: I want the cover to reflect my personality—funny, yet serious when needed. I'm open to suggestions and would love to see a design that captures the essence of the book without being too typical of the self-help genre.
Additional Information: I've attached a rough draft of the Quillmart description for more context.
Thank you for your help!
Target Market(s)
Anyone. but id say over 25
Requirements
Nice to have
- Honestly im really at a loss. Im hoping the description will help guide you. I gues i would like it to satand out of course. Be diffrent....but i know how crazy that sounds because everyone wants that. Just give me soem ideas!

```html
<!DOCTYPE html>
<html lang="en">
<head>
<meta charset="utf-8">
<title>Every Door Opens Where Every Door Opens — Book Cover</title>
<link rel="stylesheet" href="https://fonts.googleapis.com/css2?family=Bebas+Neue&family=Inter:wght@400;800;900&display=swap">
<style>
  :root {
    --page: #ffffff;
    --blue-core: #1c7ad8;
    --blue-edge: #0e56ad;
    --grid-line: rgba(255, 255, 255, 0.07);
    --sky: #6cb9ff;
    --chalk: #ffffff;
    --scene-light: rgba(235, 243, 255, 0.30);
    --scene-dim: rgba(235, 243, 255, 0.06);
  }
  * { margin: 0; padding: 0; box-sizing: border-box; }
  html, body {
    width: 1200px; height: 1200px; overflow: hidden;
    background: var(--page);
  }
  .cover {
    position: absolute;
    left: 240px; top: 60px;
    width: 720px; height: 1078px;
    overflow: hidden;
    background:
      repeating-linear-gradient(0deg, var(--grid-line) 0 1px, transparent 1px 30px),
      repeating-linear-gradient(90deg, var(--grid-line) 0 1px, transparent 1px 30px),
      radial-gradient(ellipse at 50% 45%, var(--blue-core) 0%, var(--blue-edge) 85%);
  }
  .subtitle {
    position: absolute; top: 112px; left: 0; width: 100%;
    text-align: center;
    font-family: "Inter", sans-serif;
    color: var(--sky);
    font-size: 31px; line-height: 39px;
    letter-spacing: -0.5px;
    text-transform: uppercase;
  }
  .subtitle .light { font-weight: 400; }
  .subtitle strong { font-weight: 900; }
  .balance-scene {
    position: absolute; left: 44px; top: 160px;
    width: 632px; height: 346px;
    border-radius: 12px;
    background: radial-gradient(ellipse at 50% 45%, var(--scene-light), var(--scene-dim) 75%);
  }
  .title {
    position: absolute; top: 340px; left: 0; width: 100%;
    text-align: center;
    font-family: "Bebas Neue", sans-serif;
    color: var(--chalk);
    font-size: 160px; line-height: 126px;
    letter-spacing: 2px;
  }
  .title span { display: block; }
  .tagline {
    position: absolute; top: 864px; left: 0; width: 100%;
    display: flex; justify-content: center; align-items: center; gap: 12px;
    font-family: "Bebas Neue", sans-serif;
  }
  .tagline .joiner {
    position: relative;
    color: var(--chalk);
    font-size: 50px; line-height: 50px;
    padding: 6px 0;
  }
  .tagline .joiner svg { position: absolute; left: 0; width: 100%; height: 8px; }
  .tagline .joiner .rule-top { top: -4px; }
  .tagline .joiner .rule-bottom { bottom: -4px; }
  .tagline .echo {
    color: var(--sky);
    font-size: 84px; line-height: 80px;
  }
  .author {
    position: absolute; top: 986px; left: 0; width: 100%;
    text-align: center;
    font-family: "Inter", sans-serif;
    font-weight: 900;
    color: var(--chalk);
    font-size: 48px; letter-spacing: -1px;
  }
</style>
</head>
<body>
  <main class="cover">
    <p class="subtitle">
      <span class="light">Practical Roadmap for</span><br>
      <strong>Courage</strong> <span class="light">and</span> <strong>Progress</strong>
    </p>

    <div class="balance-scene" role="img" aria-label="Sketched balance scale with a neutral-faced ball on each pan, labelled before and after, perfectly level"></div>

    <h1 class="title">
      <span>Every</span>
      <span>Door</span>
      <span>Opens</span>
    </h1>

    <div class="tagline">
      <span class="joiner">
        <svg class="rule-top" viewBox="0 0 100 8" preserveAspectRatio="none"><line x1="2" y1="4" x2="98" y2="4" stroke="#fff" stroke-width="1"/><path d="M0 4 L5 1 L5 7 Z M100 4 L95 1 L95 7 Z" fill="#fff"/></svg>
        Where
        <svg class="rule-bottom" viewBox="0 0 100 8" preserveAspectRatio="none"><line x1="2" y1="4" x2="98" y2="4" stroke="#fff" stroke-width="1"/><path d="M0 4 L5 1 L5 7 Z M100 4 L95 1 L95 7 Z" fill="#fff"/></svg>
      </span>
      <span class="echo">Every Door Opens</span>
    </div>

    <p class="author">R.K. VANTREEL</p>
  </main>
</body>
</html>
```